I need to launch a new website that more accurately reflects what we do as a business. We are an IT Reseller that specialises in delivering innovative solutions covering supply, implementation and support. My current website is www.vornetikx.com and was something I designed myself on the Hub Nimbo website. This was fine for the first 2 years but now I need something more professional and detailed. A couple of websites for companies similar to Brindle KTR are www.quarvolen.co.uk and www.ferrimund.co.uk. By looking at these it will hopefully give you an idea as to what I am trying to achieve.

Target Market(s)

UK based companies with between 30-250 employees, no fixed vertical

Coding

Coded - Design and coding required

Number of Pages Required

4 page

Font styles to use
Sans Serif

Colors
33a6d7
0592cd
85cae6

Requirements
Must have
• Contact details page to include a "Get in touch with us " section, About Us page, IT Support page to include the headings 1/ Proactive Monitoring 2/ 24 x 7 Support 3/ Security and Data Back-up 4/ Built-in Compliance (GDPR) 5/ Responsive IT Support. I am happy to provide the wording for these headings.
Clean crisp home screen with a Menu offering the requested drop down options.
Nice to have
• Easy to navigate site with a good flow. I have updated a page regarding cloud services, this would be great to have as a separate drop down menu option. I would like to have different Cloud logo's in ideally the Brindle Blue colour. Can you please add the photograph of Thornwick Lodge which is my office in the contact us page.
Should not have
• I definitely DO NOT want a photo/view of London on the home page!!

```html
<!DOCTYPE html>
<html lang="en">
<head>
<meta charset="utf-8">
<title>Brindle KTR – IT Consulting</title>
<link href="https://fonts.googleapis.com/css2?family=Montserrat:ital,wght@0,400;0,500;0,600;0,700;1,300;1,400&display=swap" rel="stylesheet">
<style>
:root{
  --blue:#0592cd;
  --blue-mid:#33a6d7;
  --blue-light:#85cae6;
  --ink:#1f2a33;
  --text:#6f7880;
  --grey-bg:#f5f6f7;
  --page-bg:#eef3f6;
  --white:#ffffff;
}
*{box-sizing:border-box;margin:0;padding:0}
html,body{width:1200px;height:4087px;overflow:hidden}
body{background:var(--page-bg);font-family:'Montserrat',sans-serif;color:var(--ink);position:relative}
.site{position:absolute;left:86px;top:170px;width:1028px;height:3898px;background:var(--white);box-shadow:0 0 30px rgba(5,146,205,.12);overflow:hidden}
.abs{position:absolute}
.center{text-align:center;left:0;right:0}
section{position:relative;width:100%}

/* nav */
.nav{height:51px;display:flex;align-items:center;padding-left:149px;background:var(--white)}
.brand{display:flex;align-items:center;gap:8px;font-weight:600;font-size:12px;color:var(--ink)}
.brand-mark{width:14px;height:14px;background:var(--blue)}
.menu{position:absolute;left:461px;top:0;height:51px;display:flex;align-items:center;gap:33px;font-size:10px;font-weight:500}
.menu a{color:var(--ink);text-decoration:none;display:flex;align-items:center;gap:4px}
.menu a.active{color:var(--blue)}

/* hero */
.hero{height:527px}
.hero-photo{position:absolute;inset:0;background:linear-gradient(135deg,#3b7fa3 0%,#1f6a92 45%,#0f5b84 100%)}
.hero-title{top:91px;font-size:32px;font-weight:600;color:var(--white)}
.hero-sub{top:172px;font-size:9.5px;line-height:16px;color:#e3f1f8}
.btn{display:inline-block;background:var(--blue);color:var(--white);font-size:9px;font-weight:600;text-align:center;border-radius:2px}
.hero-btn{position:absolute;left:465px;top:220px;width:97px;height:27px;line-height:27px}

.features{position:absolute;left:85px;top:493px;width:857px;height:167px;background:var(--white);box-shadow:0 6px 24px rgba(0,0,0,.08);display:flex;padding:34px 0;z-index:3}
.feature{flex:1;text-align:center;border-right:1px solid #dfe3e6}
.feature:last-child{border-right:none}
.feature svg{display:block;margin:0 auto 12px}
.feature h4{font-size:10px;font-weight:600;margin-bottom:10px}
.feature p{font-size:8px;line-height:12px;color:var(--text)}

/* headings */
.sec-title{font-size:28px;font-weight:600;color:var(--ink)}
.sec-sub{font-size:9px;line-height:16px;color:var(--text)}

/* about */
.about{height:596px}
.approach-title{left:149px;top:304px;font-size:17px;font-weight:600}
.approach-text{left:149px;top:331px;width:252px;font-size:8.5px;line-height:15px;color:var(--text)}
.arrows{left:149px;top:443px;display:flex;gap:18px}
.photo{background:linear-gradient(135deg,#9fb4c2,#5e7687);}
.photo.b{background:linear-gradient(135deg,#b7c6cf,#6f8796)}
.photo.c{background:linear-gradient(135deg,#c6d0d6,#7890a0)}

/* it support */
.support{height:576px;background:var(--grey-bg)}
.service{width:170px;text-align:center;transform:translateX(-85px)}
.service .ring{width:64px;height:64px;border-radius:50%;background:var(--white);box-shadow:0 4px 12px rgba(5,146,205,.15);margin:0 auto 18px;display:flex;align-items:center;justify-content:center}
.service h4{font-size:10px;font-weight:600;margin-bottom:9px}
.service p{font-size:8px;line-height:13px;color:var(--text)}
.connect{left:193px;top:448px;width:641px;height:255px;background:var(--white);box-shadow:0 4px 20px rgba(0,0,0,.07);text-align:center;z-index:3}
.connect h2{margin-top:44px;font-size:28px;font-weight:600}
.connect p{margin:14px auto 0;width:560px;font-size:9px;line-height:15px;color:var(--text)}
.connect .btn{margin-top:21px;width:95px;height:35px;line-height:35px}

/* cloud */
.cloud{height:794px}
.card{width:213px;height:163px;background:var(--grey-bg);padding:14px 12px}
.card .icon{width:50px;height:50px;border-radius:50%;background:var(--white);display:flex;align-items:center;justify-content:center}
.card .num{position:absolute;right:12px;top:14px;font-size:46px;font-weight:500;color:var(--blue-light);opacity:.55;line-height:1}
.card h4{position:absolute;left:12px;top:80px;font-size:12px;font-weight:600}
.card p{position:absolute;left:12px;top:110px;width:185px;font-size:8px;line-height:13px;color:var(--text)}
.card.active{background:var(--blue)}
.card.active h4,.card.active p{color:var(--white)}
.card.active .num{color:var(--white);opacity:.25}

/* testimonials */
.testimonials{height:1133px;background:var(--grey-bg)}
.quote{top:270px;font-size:18.5px;line-height:29px;font-style:italic;font-weight:300;color:var(--ink)}
.author{top:374px;font-size:12px;font-weight:600;color:var(--blue)}
.author span{font-size:9px;font-weight:400}
.map{left:0;top:755px;width:1028px;height:378px;background:linear-gradient(160deg,#dfe8e3 0%,#e8ede6 50%,#d6e2dc 100%)}
.contact{left:149px;top:471px;width:730px;height:359px;background:var(--white);display:flex;z-index:3;box-shadow:0 4px 20px rgba(0,0,0,.08)}
.contact-form{width:308px;position:relative}
.contact-form h3{position:absolute;left:36px;top:66px;font-size:15px;font-weight:600;line-height:19px}
.field{position:absolute;left:36px;width:238px;background:var(--grey-bg);font-size:7px;color:#8a9299;padding:9px 14px}
.contact-photo{flex:1;background:linear-gradient(180deg,#8fb3cf 0%,#9b5b43 45%,#7d4a38 70%,#6f8a4c 100%)}

/* footer */
.footer{height:221px;background:var(--blue);color:var(--white)}
.footer .brand{color:var(--white)}
.footer .brand-mark{background:var(--white)}
.f-line{font-size:7px;line-height:11px;display:flex;align-items:flex-start;gap:8px}
.f-links{left:433px;top:50px;font-size:8px;line-height:19.5px}
.f-news{left:634px;top:49px;font-size:9px;font-weight:600}
.f-input{left:634px;top:73px;width:146px;height:35px;background:var(--white);color:var(--ink);font-size:7.5px;padding:13px 19px}
.f-btn{left:780px;top:73px;width:99px;height:35px;background:#1d2a35;font-size:9px;line-height:35px;text-align:center;font-weight:500}
.f-bottom{left:149px;right:149px;top:165px;font-size:6.5px;display:flex;justify-content:space-between}
</style>
</head>
<body>
<div class="site">

  <nav class="nav">
    <div class="brand"><span class="brand-mark"></span>Brindle KTR</div>
    <div class="menu">
      <a class="active">Home</a>
      <a>About Us</a>
      <a>IT Support <svg width="7" height="5" viewBox="0 0 7 5"><path d="M1 1l2.5 2.5L6 1" stroke="#1f2a33" fill="none"/></svg></a>
      <a>Cloud Adoption <svg width="7" height="5" viewBox="0 0 7 5"><path d="M1 1l2.5 2.5L6 1" stroke="#1f2a33" fill="none"/></svg></a>
      <a>Contact Us</a>
    </div>
  </nav>

  <section class="hero">
    <div class="hero-photo" role="img" aria-label="Team of colleagues joining hands over a meeting table, blue-tinted office photo"></div>
    <h1 class="abs center hero-title" style="text-align:center">Experienced, Personalised IT Consulting</h1>
    <p class="abs center hero-sub" style="text-align:center">We understand that no two businesses are the same so why should the service delivered be any different.<br>We aim to understand all your business drivers so advise you every step of the way.</p>
    <a class="btn hero-btn">Get Started</a>
  </section>

  <div class="features">
    <div class="feature">
      <svg width="18" height="18" viewBox="0 0 18 18"><circle cx="9" cy="9" r="7.5" fill="none" stroke="#0592cd"/><path d="M9 5v4l3 2" stroke="#0592cd" fill="none"/></svg>
      <h4>Save Time</h4><p>We can allow you to<br>focus solely on growing</p>
    </div>
    <div class="feature">
      <svg width="22" height="18" viewBox="0 0 22 18"><circle cx="9" cy="9" r="7" fill="none" stroke="#0592cd"/><path d="M9 5v4h3M15 12l5 4" stroke="#0592cd" fill="none"/></svg>
      <h4>24/7 Support</h4><p>Allow us to deliver the<br>support and expertise.</p>
    </div>
    <div class="feature">
      <svg width="18" height="18" viewBox="0 0 18 18"><path d="M2 16h14M3 13l4-4 3 3 6-7M12 5h4v4" stroke="#0592cd" fill="none"/></svg>
      <h4>Budgeting</h4><p>Take out the support<br>contract that best suits</p>
    </div>
    <div class="feature">
      <svg width="20" height="18" viewBox="0 0 20 18"><rect x="7" y="1" width="6" height="5" fill="none" stroke="#0592cd"/><path d="M10 6v4M3 10h14M3 10v3M10 10v3M17 10v3" stroke="#0592cd" fill="none"/><rect x="1" y="13" width="4" height="4" fill="none" stroke="#0592cd"/><rect x="8" y="13" width="4" height="4" fill="none" stroke="#0592cd"/><rect x="15" y="13" width="4" height="4" fill="none" stroke="#0592cd"/></svg>
      <h4>Risk Management</h4><p>Leave us to protect your<br>business, if there is an</p>
    </div>
  </div>

  <section class="about">
    <h2 class="abs center sec-title" style="top:166px;text-align:center">About Us</h2>
    <p class="abs center sec-sub" style="top:209px;text-align:center">We understand that no two businesses are the same so why should the service delivered be any different.<br>We aim to understand all your business drivers so advise you every step of the way.</p>
    <h3 class="abs approach-title">Our Approach</h3>
    <p class="abs approach-text">We understand that no two businesses are the same so why should the service delivered be any different. We aim to understand all your business drivers so we can not only add a world class services but be there to advise you every step of the way.</p>
    <div class="abs arrows">
      <svg width="17" height="17" viewBox="0 0 17 17"><circle cx="8.5" cy="8.5" r="7.5" fill="none" stroke="#0592cd"/><path d="M10 5L6.5 8.5 10 12" stroke="#0592cd" fill="none"/></svg>
      <svg width="17" height="17" viewBox="0 0 17 17"><circle cx="8.5" cy="8.5" r="7.5" fill="none" stroke="#0592cd" stroke-width="1.5"/><path d="M5 8.5h7M9 5.5l3 3-3 3" stroke="#0592cd" fill="none" stroke-width="1.5"/></svg>
    </div>
    <div class="abs photo" style="left:519px;top:293px;width:228px;height:165px" role="img" aria-label="Colleagues in a meeting around a laptop"></div>
    <div class="abs photo b" style="left:769px;top:363px;width:110px;height:79px" role="img" aria-label="Small team discussion at a desk"></div>
    <div class="abs photo c" style="left:687px;top:442px;width:146px;height:73px" role="img" aria-label="Business people at a conference table"></div>
  </section>

  <section class="support">
    <h2 class="abs center sec-title" style="top:79px;text-align:center">IT Support - Infrastructure Support</h2>
    <p class="abs center sec-sub" style="top:124px;font-size:8.5px;text-align:center">Using A Pro Fessional And Friendly IT Support Company To Look After Your IT Infrastructure Is A Cost Effective Way To Have All The Skills<br>Available When Needed, But Without Having The Overheads Associated With Full Time Staff.</p>
    <div class="abs service" style="left:225px;top:208px">
      <div class="ring"><svg width="34" height="22" viewBox="0 0 34 22"><path d="M2 11C8 3 26 3 32 11 26 19 8 19 2 11z" fill="none" stroke="#0592cd" stroke-width="1.5"/><circle cx="17" cy="11" r="5" fill="none" stroke="#0592cd" stroke-width="1.5"/></svg></div>
      <h4>Proactive Monitoring</h4><p>We can allow you to focus solely on growing and developing your business.</p>
    </div>
    <div class="abs service" style="left:417px;top:208px">
      <div class="ring"><svg width="24" height="28" viewBox="0 0 24 28"><path d="M12 2l9 4v8c0 6-4 10-9 12-5-2-9-6-9-12V6z" fill="none" stroke="#0592cd" stroke-width="1.5"/><rect x="8" y="12" width="8" height="6" fill="none" stroke="#0592cd"/><path d="M9.5 12V10a2.5 2.5 0 0 1 5 0v2" fill="none" stroke="#0592cd"/></svg></div>
      <h4>Security and Data Back-up</h4><p>We can allow you to focus solely on growing and developing your business.</p>
    </div>
    <div class="abs service" style="left:609px;top:208px">
      <div class="ring"><svg width="28" height="28" viewBox="0 0 28 28"><circle cx="14" cy="11" r="8" fill="none" stroke="#0592cd" stroke-width="1.5"/><path d="M10 11l3 3 5-6M4 26c2-5 6-7 10-7s8 2 10 7" fill="none" stroke="#0592cd" stroke-width="1.5"/></svg></div>
      <h4>Built-in Compliance (GDPR)</h4><p>We can allow you to focus solely on growing and developing your business.</p>
    </div>
    <div class="abs service" style="left:803px;top:208px">
      <div class="ring"><svg width="28" height="28" viewBox="0 0 28 28"><circle cx="14" cy="14" r="12" fill="none" stroke="#0592cd" stroke-width="1.5"/><circle cx="14" cy="14" r="7" fill="none" stroke="#0592cd" stroke-width="1.5"/><circle cx="14" cy="12" r="2.5" fill="none" stroke="#0592cd"/><path d="M10 19c1-3 7-3 8 0" fill="none" stroke="#0592cd"/></svg></div>
      <h4>Responsive IT Support</h4><p>We can allow you to focus solely on growing and developing your business.</p>
    </div>
    <div class="abs connect">
      <h2>Let's Get Connected</h2>
      <p>"To Keep Your Costs Down Brindle KTR Provides Flexible Options That Fit Your Requirements And Budgets, From Pre-Paid To Fully Managed Support. We Deliver Cost Effective IT Support For Companies Whether You Are Setup For Remote Working Or Are Office Based.We Can Also Tailor A Support Package Specifically For Your Business, So Please Call Us For A Chat Without Any Obligation On 01632 960418"</p>
      <a class="btn">Call Now</a>
    </div>
  </section>

  <section class="cloud">
    <h2 class="abs center sec-title" style="top:211px;text-align:center">Cloud Adoption</h2>
    <p class="abs center sec-sub" style="top:256px;text-align:center">We understand that no two businesses are the same so why should the service delivered be any different.<br>We aim to understand all your business drivers so advise you every step of the way.</p>

    <div class="abs card active" style="left:149px;top:340px">
      <div class="icon"><svg width="26" height="26" viewBox="0 0 26 26"><circle cx="9" cy="9" r="5" fill="none" stroke="#0592cd" stroke-width="1.5"/><circle cx="17" cy="17" r="5" fill="none" stroke="#0592cd" stroke-width="1.5"/><circle cx="17" cy="17" r="1.5" fill="#0592cd"/></svg></div>
      <span class="num">1</span><h4>Services. Perfectly Managed</h4>
      <p>We employ Managed Services to significantly streamline your business, tailoring your solutions to meet digital market demands.</p>
    </div>
    <div class="abs card" style="left:408px;top:340px">
      <div class="icon"><svg width="26" height="26" viewBox="0 0 26 26"><path d="M20 10a8 8 0 1 0 1 5" fill="none" stroke="#0592cd" stroke-width="1.5"/><path d="M21 5v5h-5" fill="none" stroke="#0592cd" stroke-width="1.5"/><circle cx="13" cy="13" r="3" fill="none" stroke="#0592cd"/></svg></div>
      <span class="num">2</span><h4>Fail Fast with the Cloud</h4>
      <p>Prototype your new business features within less than a week &amp; without having to invest a single penny.</p>
    </div>
    <div class="abs card" style="left:666px;top:340px">
      <div class="icon"><svg width="30" height="24" viewBox="0 0 30 24"><path d="M8 19a6 6 0 0 1 0-12 8 8 0 0 1 15 2 5 5 0 0 1 0 10z" fill="none" stroke="#0592cd" stroke-width="1.5"/><path d="M12 17v-3M15 17v-5M18 17v-7" stroke="#0592cd" stroke-width="1.5"/></svg></div>
      <span class="num">3</span><h4>Improve your ROI</h4>
      <p>Using the Cloud, we launch your product to market quickly and cost-effectively - making sure it's future-proof, scalable, reliable, and</p>
    </div>
    <div class="abs card" style="left:279px;top:549px">
      <div class="icon"><svg width="30" height="24" viewBox="0 0 30 24"><path d="M8 19a6 6 0 0 1 0-12 8 8 0 0 1 15 2 5 5 0 0 1 0 10z" fill="none" stroke="#0592cd" stroke-width="1.5"/><circle cx="15" cy="12" r="2.5" fill="none" stroke="#0592cd"/><path d="M11 18c1-3 7-3 8 0" fill="none" stroke="#0592cd"/></svg></div>
      <span class="num">4</span><h4>The Cloud Dream Team</h4>
      <p>They'll have thorough understanding of the project's scope. They'll see the bigger picture and understand the business value you want</p>
    </div>
    <div class="abs card" style="left:538px;top:549px">
      <div class="icon"><svg width="26" height="26" viewBox="0 0 26 26"><ellipse cx="9" cy="8" rx="5" ry="2" fill="none" stroke="#0592cd" stroke-width="1.5"/><path d="M4 8v10c0 1 2 2 5 2s5-1 5-2V8M4 13c0 1 2 2 5 2s5-1 5-2" fill="none" stroke="#0592cd" stroke-width="1.5"/><circle cx="19" cy="9" r="3" fill="none" stroke="#0592cd" stroke-width="1.5"/><path d="M16 14h6v6h-6z" fill="none" stroke="#0592cd" stroke-width="1.5"/></svg></div>
      <span class="num">5</span><h4>The Business Benefits</h4>
      <p>Make informed decisions about the product's development pipeline. Save costs as you'll spend less time on redefining requirements.</p>
    </div>
  </section>

  <section class="testimonials">
    <h2 class="abs center sec-title" style="top:80px;text-align:center">Testimonials</h2>
    <p class="abs center" style="top:128px;font-size:8px;text-align:center;color:var(--ink)">What our clint say about us</p>
    <svg class="abs" style="left:491px;top:208px" width="46" height="44" viewBox="0 0 46 44"><path d="M20 40V18A14 14 0 0 0 6 4M42 40V18A14 14 0 0 0 28 4" fill="none" stroke="#0592cd" stroke-width="2.5"/><path d="M6 4A8 8 0 1 0 20 18M28 4A8 8 0 1 0 42 18" fill="none" stroke="#0592cd" stroke-width="2.5"/></svg>
    <p class="abs center quote" style="text-align:center">Our extensive equipment fleet, along with our modern maintenance and<br>fabrication facility allow us the ability to support our diverse workforce and<br>our capable partners whenever necessary.</p>
    <p class="abs center author" style="text-align:center">Oliver Pennick <span>- Fenwick Client</span></p>
    <svg class="abs" style="left:149px;top:374px" width="17" height="17" viewBox="0 0 17 17"><circle cx="8.5" cy="8.5" r="7.5" fill="none" stroke="#0592cd" stroke-width="1.5"/><path d="M12 8.5H5M8 5.5l-3 3 3 3" stroke="#0592cd" fill="none" stroke-width="1.5"/></svg>
    <svg class="abs" style="left:862px;top:374px" width="17" height="17" viewBox="0 0 17 17"><circle cx="8.5" cy="8.5" r="7.5" fill="none" stroke="#0592cd" stroke-width="1.5"/><path d="M5 8.5h7M9 5.5l3 3-3 3" stroke="#0592cd" fill="none" stroke-width="1.5"/></svg>

    <div class="abs map" role="img" aria-label="Street map of the area around the office with a location pin"></div>

    <div class="abs contact">
      <div class="contact-form">
        <h3>Get in touch<br>with us</h3>
        <div class="field" style="top:127px;height:29px">Your Name</div>
        <div class="field" style="top:160px;height:29px">Phone Number</div>
        <div class="field" style="top:192px;height:56px;padding-top:16px">Write Message</div>
        <a class="btn abs" style="left:36px;top:267px;width:79px;height:27px;line-height:27px;font-size:8px">Get Started</a>
      </div>
      <div class="contact-photo" role="img" aria-label="Thornwick Lodge, a red-brick manor house office beside a lawn under blue sky"></div>
    </div>
  </section>

  <footer class="footer abs" style="left:0;top:3677px;width:1028px">
    <div class="brand abs" style="left:149px;top:52px"><span class="brand-mark"></span>Brindle KTR</div>
    <div class="f-line abs" style="left:149px;top:96px">
      <svg width="9" height="9" viewBox="0 0 9 9"><path d="M2 1l2 2-1 1.5a5 5 0 0 0 1.5 1.5L6 5l2 2-1.5 1.5C4 8 1 5 .5 2z" fill="#fff"/></svg>01632 960418</div>
    <div class="f-line abs" style="left:149px;top:118px">
      <svg width="9" height="11" viewBox="0 0 9 11"><path d="M4.5 11S1 6.5 1 4.5a3.5 3.5 0 0 1 7 0C8 6.5 4.5 11 4.5 11z" fill="#fff"/><circle cx="4.5" cy="4.5" r="1.3" fill="#0592cd"/></svg>
      <span>Thornwick Lodge, Marlow Fenby,<br>Ashcombe, Hertfordshire, AL9 4QT</span></div>
    <div class="abs f-links">Home<br>About Us<br>IT Support<br>Cloud Adoption<br>Contact Us</div>
    <div class="abs f-news">Get the freshest news from us</div>
    <div class="abs f-input">Your email address...</div>
    <div class="abs f-btn">Subscribe</div>
    <div class="abs f-bottom"><span>Terms &amp; Conditions &nbsp;&nbsp;|&nbsp;&nbsp; Privacy Policy &nbsp;&nbsp;|&nbsp;&nbsp; Accessibility &nbsp;&nbsp;|&nbsp;&nbsp; Legal</span><span>Brindle KTR 2020. All right reserved</span></div>
  </footer>

</div>
</body>
</html>
```